Djent/ Neoclassical band needs album cover

This album is going to be for an EP that will consist of a bunch of singles released about a month apart from each other. The band is called Tarn.vel and the EP title will tentatively be called Hollow Tidewater, but I will probably replace the text for each song on the album cover and upload it that way.

It's mostly female ethereal sounding vocals with male rough singing and screaming. Heavy metal drums with some melodic interludes and electronic components as well.

The biggest thing is I'm going to need to redo the album cover so that it changes ever so slightly from cover to cover. If you want an example of what I'm talking about, you can check out my other band Nine Acre Rooftop. I took a cover from Sketch hive and imposed different colors over it so that It made each single different while still feeling like a cohesive effort on one project. So either the cover will have to be flexible enough for me to adjust, or you can create 4 different simple covers.

I have no restrictions on subject material. I like nature, geometric designs, modern looking metal covers. The only thing I don't like would be anything slated towards violence, blood, satanic sacrifices, we are not that kind of metal band haha.

I realize a lot of people are creating designs based on the images that I posted. I don't want a door or that style of album cover, I was only posting that to show you how I created 4 different album covers from one design. I don't want the same design for an album cover, or anything even close since I already have a band with that cover.

Target Market(s)

Males 18-40

Requirements
Must have
• Easily manipulated design or 4 slightly different designs.
Should not have
• Violence

```html
<!DOCTYPE html>
<html lang="en">
<head>
<meta charset="utf-8">
<title>Tarn.vel — Hollow Tidewater</title>
<link rel="stylesheet" href="https://fonts.googleapis.com/css2?family=Bebas+Neue&family=Poppins:wght@300;600&display=swap">
<style>
  :root {
    --page-bg: #d3d3d5;
    --sky-dark: #14403b;
    --sky-mist: #5f9d94;
    --mountain: #2f5e44;
    --mountain-deep: #1f4532;
    --water: #183832;
    --glow-top: #5aaea2;
    --glow-bottom: #c4e8e2;
    --ink-light: #ffffff;
  }
  html, body {
    margin: 0;
    padding: 0;
    width: 750px;
    height: 1200px;
    overflow: hidden;
    background: var(--page-bg);
  }
  .canvas {
    position: relative;
    width: 750px;
    height: 1200px;
  }
  .album-cover {
    position: absolute;
    left: 75px;
    top: 300px;
    width: 600px;
    height: 600px;
    box-shadow: 14px 16px 22px rgba(0, 0, 0, 0.45);
  }
  .album-cover svg {
    display: block;
    width: 600px;
    height: 600px;
  }
  .band-name {
    font-family: "Bebas Neue", sans-serif;
    font-size: 22px;
    letter-spacing: 10px;
    fill: var(--ink-light);
  }
  .title-light {
    font-family: "Poppins", sans-serif;
    font-weight: 300;
    font-size: 36px;
    fill: var(--ink-light);
  }
  .title-bold {
    font-family: "Poppins", sans-serif;
    font-weight: 600;
    font-size: 50px;
    fill: var(--ink-light);
  }
  .title-reflection {
    opacity: 0.12;
  }
</style>
</head>
<body>
<main class="canvas">
  <figure class="album-cover" style="margin:0">
    <svg viewBox="0 0 600 600" xmlns="http://www.w3.org/2000/svg">
      <defs>
        <linearGradient id="landscape-tones" x1="0" y1="0" x2="0" y2="1">
          <stop offset="0" stop-color="var(--sky-dark)"/>
          <stop offset="0.38" stop-color="var(--sky-mist)"/>
          <stop offset="0.58" stop-color="var(--mountain)"/>
          <stop offset="0.83" stop-color="var(--mountain-deep)"/>
          <stop offset="1" stop-color="var(--water)"/>
        </linearGradient>
        <linearGradient id="triangle-glow" x1="0" y1="0" x2="0" y2="1">
          <stop offset="0" stop-color="var(--glow-top)"/>
          <stop offset="0.6" stop-color="var(--glow-bottom)"/>
          <stop offset="0.75" stop-color="var(--mountain)"/>
          <stop offset="1" stop-color="var(--mountain-deep)"/>
        </linearGradient>
      </defs>

      <rect class="cover-photo" width="600" height="600" fill="url(#landscape-tones)"
            role="img" aria-label="Misty green mountain valley above a dark lake under a stormy teal sky"/>

      <polygon class="frame-triangle" points="124,122 484,122 305,432"
               fill="url(#triangle-glow)" fill-opacity="0.85"
               stroke="var(--ink-light)" stroke-width="1.5"
               role="img" aria-label="Brighter glowing sky seen through the triangle"/>

      <text class="band-name" x="305" y="68" text-anchor="middle">TARN.VEL</text>

      <text class="title-light" x="300" y="497" text-anchor="middle"
            textLength="280" lengthAdjust="spacing">HOLLOW</text>
      <text class="title-bold" x="300" y="545" text-anchor="middle"
            textLength="280" lengthAdjust="spacingAndGlyphs">TIDEWATER</text>
      <text class="title-bold title-reflection" x="300" y="-552" text-anchor="middle"
            transform="scale(1,-1)" textLength="280" lengthAdjust="spacingAndGlyphs"
            aria-hidden="true">TIDEWATER</text>
    </svg>
  </figure>
</main>
</body>
</html>
```